Tarvell homes and renovations business card design.

Would like some new card designs utilizing my new logo that look professional. I am open to different colors on the logo or utilize the same ones we have. I like the original concept but would like to see some fresh ideas and build on what we have already done.

Target Market(s)

Custom home building industry, Real estate sales, Renovation projects.

Industry/Entity Type

Home Builder

Contact Information for Business Card

Tarvell Homes and Renovations
2871 162nd Street
Frank, Alberta
T0L3P0
Home : 403- 555-0187 Cell: 403- 555-0243

My info is : Gus Tarvell, President and CEO
email: tarvellhomes@quillmail.example
Website: tarvellhomes.example

Requirements
Must have
• Must Use my new logo design. I am open to different colors on the logo or utilize the same ones in the existing design. I can upload the original logo design if needed.

```html
<!DOCTYPE html>
<html lang="en">
<head>
<meta charset="utf-8">
<title>Tarvell Homes and Renovations – Business Card</title>
<link rel="stylesheet" href="https://fonts.googleapis.com/css2?family=Roboto:wght@400;500&display=swap">
<style>
  :root {
    --page-bg: #ececea;
    --front-orange: #d8900e;
    --back-black: #0b0b0b;
    --back-charcoal: #1c1c1c;
    --brand-gold: #bb8a28;
    --line-gold: #c9961f;
    --ink-white: #ffffff;
    --ink-black: #0a0a0a;
    --faint-grey: #3a3a3a;
  }
  * { box-sizing: border-box; margin: 0; padding: 0; }
  html, body { width: 1200px; height: 1200px; overflow: hidden; }
  body {
    background: var(--page-bg);
    font-family: "Roboto", Arial, sans-serif;
    display: flex;
    flex-direction: column;
    align-items: center;
    justify-content: center;
    gap: 60px;
  }
  .card {
    position: relative;
    width: 900px;
    height: 514px;
    border-radius: 22px;
    overflow: hidden;
    box-shadow: 0 6px 18px rgba(0,0,0,0.18);
  }

  /* Front */
  .card-front {
    background: var(--front-orange);
    display: flex;
    align-items: center;
    justify-content: center;
  }
  .front-wordmark {
    color: var(--ink-white);
    font-weight: 400;
    text-align: center;
    line-height: 1;
  }
  .front-wordmark .brand-name {
    display: block;
    font-size: 96px;
    letter-spacing: 4px;
    text-transform: uppercase;
  }
  .front-wordmark .brand-tagline {
    display: block;
    margin-top: 10px;
    font-size: 28px;
    letter-spacing: 1px;
    text-transform: uppercase;
  }

  /* Back */
  .card-back {
    background: linear-gradient(135deg, var(--back-black) 0%, var(--back-charcoal) 100%);
  }
  .back-wordmark {
    position: absolute;
    left: 70px;
    top: 120px;
    color: var(--brand-gold);
    font-weight: 400;
    line-height: 1;
  }
  .back-wordmark .brand-name {
    display: block;
    font-size: 66px;
    letter-spacing: 3px;
    text-transform: uppercase;
  }
  .back-wordmark .brand-tagline {
    display: block;
    margin-top: 8px;
    font-size: 19px;
    text-transform: uppercase;
  }
  .trade-icons {
    position: absolute;
    right: 40px;
    top: 0;
    width: 420px;
    height: 250px;
    border-left: 1px dashed var(--faint-grey);
    display: grid;
    grid-template-columns: repeat(3, 1fr);
    grid-template-rows: 1fr 1fr;
  }
  .trade-cell {
    border-right: 1px dashed var(--faint-grey);
    border-bottom: 1px dashed var(--faint-grey);
    display: flex;
    align-items: center;
    justify-content: center;
  }
  .trade-cell .icon-area {
    width: 78px;
    height: 78px;
    border-radius: 8px;
    background: rgba(255,255,255,0.06);
  }
  .stripe-set {
    position: absolute;
    left: 0;
    right: 0;
    top: 300px;
  }
  .stripe { height: 6px; background: var(--line-gold); }
  .stripe.dark { height: 10px; background: var(--ink-black); }
  .stripe-gap { height: 10px; }
  .contact-band {
    position: absolute;
    left: 0;
    right: 0;
    bottom: 0;
    top: 342px;
    background: var(--brand-gold);
    display: flex;
    align-items: center;
    justify-content: space-around;
    padding: 0 40px;
  }
  .contact-item {
    display: flex;
    align-items: center;
    gap: 14px;
    color: var(--ink-black);
    font-size: 20px;
    line-height: 1.3;
  }
  .contact-icon {
    width: 44px;
    height: 44px;
    border-radius: 50%;
    background: var(--ink-black);
    display: flex;
    align-items: center;
    justify-content: center;
    flex-shrink: 0;
  }
  .contact-item address { font-style: normal; }
</style>
</head>
<body>

  <section class="card card-front" aria-label="Card front">
    <div class="front-wordmark">
      <span class="brand-name">Tarvell</span>
      <span class="brand-tagline">Homes and Renovations</span>
    </div>
  </section>

  <section class="card card-back" aria-label="Card back">
    <div class="back-wordmark">
      <span class="brand-name">Tarvell</span>
      <span class="brand-tagline">Homes and Renovations</span>
    </div>

    <div class="trade-icons">
      <div class="trade-cell"><div class="icon-area" role="img" aria-label="Faint line icon of a hand holding a hammer"></div></div>
      <div class="trade-cell"><div class="icon-area" role="img" aria-label="Faint line icon of a hard hat"></div></div>
      <div class="trade-cell"><div class="icon-area" role="img" aria-label="Faint line icon of crossed wrench and screwdriver"></div></div>
      <div class="trade-cell"></div>
      <div class="trade-cell"></div>
      <div class="trade-cell"></div>
    </div>

    <div class="stripe-set">
      <div class="stripe"></div>
      <div class="stripe-gap"></div>
      <div class="stripe dark"></div>
      <div class="stripe-gap"></div>
      <div class="stripe"></div>
    </div>

    <div class="contact-band">
      <div class="contact-item">
        <span class="contact-icon">
          <svg width="22" height="22" viewBox="0 0 24 24" aria-hidden="true">
            <path d="M12 2a7 7 0 0 0-7 7c0 5 7 13 7 13s7-8 7-13a7 7 0 0 0-7-7z" fill="none" stroke="#fff" stroke-width="2"/>
            <circle cx="12" cy="9" r="2.5" fill="#fff"/>
          </svg>
        </span>
        <address>2871 162nd Street Frank,<br>Alberta T0L3P0</address>
      </div>
      <div class="contact-item">
        <span class="contact-icon">
          <svg width="22" height="22" viewBox="0 0 24 24" aria-hidden="true">
            <path d="M3 9c0-3 4-5 9-5s9 2 9 5v2h-5V9H8v2H3z" fill="#fff"/>
            <path d="M6 12h12l2 8H4z" fill="#fff"/>
            <circle cx="12" cy="16" r="2.2" fill="#0a0a0a"/>
          </svg>
        </span>
        <span>403- 555-0243</span>
      </div>
      <div class="contact-item">
        <span class="contact-icon">
          <svg width="22" height="22" viewBox="0 0 24 24" aria-hidden="true">
            <path d="M6.6 10.8a15 15 0 0 0 6.6 6.6l2.2-2.2c.3-.3.7-.4 1-.2 1.1.4 2.3.6 3.6.6.6 0 1 .4 1 1V20c0 .6-.4 1-1 1A17 17 0 0 1 3 4c0-.6.4-1 1-1h3.5c.6 0 1 .4 1 1 0 1.3.2 2.5.6 3.6.1.3 0 .7-.2 1z" fill="#fff"/>
          </svg>
        </span>
        <span>403- 555-0187</span>
      </div>
    </div>
  </section>

</body>
</html>
```